We are an Estate agency (Real estate)– looking for Christmas/winter theme leaflet

We are called ‘’HOLLIVERS’’ we are an estate agency based in England. We opened in 2020 in February, few weeks before Covid and we are now known as one of the fastest growing agencies in all of Brighton and Hove.
This is our first Christmas/winter leaflet and this kind of offer!
Offer is: if the client signs with us to sell their home from 1st December 2021 until 7th January 2022 they will receive 50% off HOLLIVERS fees.
I am looking for A5 two-sided leaflet. The first side should contain our branding, the offer. Also, maybe this: ‘’ Let us Treat you this Christmas’’ or maybe on the other side of leaflet, which will contain explanation of the offer, our office details etc. the back should also contain some design.
Our target market is higher end clients who own a property in Brighton and Hove and looking to sell. I would say target market 35+ years of age.
Our branding is clean, fresh and eye catching and that’s what leaflet should look like and represent.
I will insert our website link so you could have a look at the properties that we deal with too. I could also insert last leaflet which I designed and had a really positive response & feedback… maybe will give you some ideas.
I have inserted our brand guidelines. We use Hollivers in white or blue backgrounds as in guideline.
https://www.holliversestateagents.co.uk/
Hi guys,
Thank you for all your ideas so far, however just wanted to mention that I am looking for not so much ''in your face Christmas'' design - something subtle.
Needs to be classy, modern and eye catching - our target market is property owners 35+ years of age. Moreover, this offer needs to be perceived as one off opportunity.
35+ property owners

```html
<!DOCTYPE html>
<html lang="en">
<head>
<meta charset="utf-8">
<title>Hollivers – Christmas Leaflet</title>
<link href="https://fonts.googleapis.com/css2?family=Ubuntu:wght@400;500;700&display=swap" rel="stylesheet">
<style>
  :root{
    --backdrop:#7a96aa;
    --navy:#002845;
    --magenta:#d6098a;
    --white:#ffffff;
    --frost:#b9c6d1;
  }
  *{box-sizing:border-box;margin:0;padding:0}
  html,body{width:1200px;height:1200px;overflow:hidden}
  body{background:var(--backdrop);font-family:'Ubuntu',sans-serif;position:relative}

  .leaflet{position:absolute;top:234px;width:485px;height:690px;overflow:hidden;box-shadow:4px 6px 10px rgba(0,0,0,.25)}
  .leaflet--front{left:86px;background:var(--navy)}
  .leaflet--back{left:622px;background:var(--white)}

  .frost-border{position:absolute;left:0;top:0;width:100%;height:112px}
  .leaflet--front .frost-border{background:linear-gradient(to bottom,#eef2f5 0%,var(--frost) 30%,#5c7790 65%,var(--navy) 100%)}
  .leaflet--back .frost-border{background:linear-gradient(to bottom,var(--navy) 0%,#3f5f7a 30%,var(--frost) 70%,var(--white) 100%)}

  /* front */
  .brand-name{position:absolute;left:0;width:100%;text-align:center;color:var(--white);font-weight:500;white-space:nowrap}
  .leaflet--front .brand-name{top:362px;font-size:33px;letter-spacing:6px}
  .offer-band{position:absolute;left:0;top:474px;width:100%;height:55px;background:var(--magenta);color:var(--white);font-weight:700;font-size:23px;letter-spacing:1px;text-align:center;line-height:55px;white-space:nowrap}
  .sparkle{position:absolute;border-radius:50%}
  .leaflet--front .sparkle{left:229px;top:583px;width:26px;height:26px;background:radial-gradient(circle,#f7e6ee 0%,#b7a2b6 45%,rgba(0,40,69,0) 75%)}
  .social{position:absolute;left:204px;top:652px;display:flex;gap:7px}
  .social span{width:21px;height:21px;border:1.5px solid var(--white);border-radius:50%}

  /* back */
  .treat-line{position:absolute;left:0;width:100%;top:122px;text-align:center}
  .treat-line span{display:inline-block;color:var(--navy);font-weight:500;font-size:18px;padding-bottom:3px;border-bottom:2px solid var(--navy)}
  .leaflet--back .sparkle{left:233px;width:20px;height:20px;background:radial-gradient(circle,var(--navy) 0%,#6d8aa2 45%,rgba(255,255,255,0) 75%)}
  .headline{position:absolute;left:0;width:100%;text-align:center;font-weight:700;color:var(--navy);line-height:1;white-space:nowrap}
  .headline--sign{top:217px;font-size:29px;letter-spacing:1px}
  .headline--sell{top:272px;font-size:29px;letter-spacing:1px;color:var(--magenta)}
  .headline--fees{top:328px;font-size:23px;letter-spacing:.5px}
  .tick{position:absolute;left:242px;width:2.5px;height:8px;background:var(--navy)}
  .validity{position:absolute;left:0;width:100%;top:415px;text-align:center;font-size:11.5px;color:var(--navy)}

  .listings{position:absolute;left:0;top:446px;width:100%;height:121px;display:flex;gap:4px}
  .listing{position:relative;flex:1;overflow:hidden}
  .listing--a{background:linear-gradient(to bottom,#8fb4dc 0%,#b6674a 45%,#7f8d61 75%,#8a7d72 100%)}
  .listing--b{background:linear-gradient(to bottom,#6d9ad3 0%,#e7eaea 40%,#6f8a5a 70%,#9a9a98 100%)}
  .listing--c{background:linear-gradient(to bottom,#89b2df 0%,#c25f3f 35%,#eceeee 65%,#9d9990 100%)}
  .sold-tag{position:absolute;left:12px;top:16px;background:var(--magenta);color:var(--white);font-weight:700;font-size:13px;letter-spacing:.5px;padding:2px 10px;transform:rotate(-18deg)}
  .captions{position:absolute;left:0;top:567px;width:100%;height:19px;background:var(--magenta);display:flex;gap:4px}
  .captions span{flex:1;color:var(--white);font-size:7.6px;text-align:center;line-height:19px;white-space:nowrap}

  .contact-footer{position:absolute;left:0;top:586px;width:100%;height:104px;background:var(--navy)}
  .contact-footer .brand-name{left:20px;width:121px;top:46px;font-size:11px;letter-spacing:2px;font-weight:700}
  .divider{position:absolute;left:161px;top:16px;width:2.5px;height:72px;background:var(--white)}
  .contact-details{position:absolute;left:211px;top:23px;list-style:none;color:var(--white);font-size:11.5px;line-height:20.5px}
</style>
</head>
<body>

<section class="leaflet leaflet--front">
  <div class="frost-border" role="img" aria-label="Decorative border of white and frosted snowflakes"></div>
  <div class="brand-name">HOLLIVERS</div>
  <div class="offer-band">GET 50% OFF HOLLIVERS FEES</div>
  <div class="sparkle" role="img" aria-label="Small pale snowflake"></div>
  <div class="social" aria-label="Social media links"><span></span><span></span><span></span></div>
</section>

<section class="leaflet leaflet--back">
  <div class="frost-border" role="img" aria-label="Decorative border of navy and frosted snowflakes"></div>
  <p class="treat-line"><span>Let us treat you this Christmas.</span></p>
  <div class="sparkle" style="top:174px" role="img" aria-label="Small navy snowflake"></div>
  <h1 class="headline headline--sign">SIGN WITH US</h1>
  <div class="tick" style="top:255px"></div>
  <h2 class="headline headline--sell">SELL YOUR HOME</h2>
  <div class="tick" style="top:309px"></div>
  <h2 class="headline headline--fees">AND GET 50% OFF HOLLIVERS FEES</h2>
  <div class="sparkle" style="top:371px" role="img" aria-label="Small navy snowflake"></div>
  <p class="validity">Offer valid from 1st December 2021 until 7th January 2022</p>

  <div class="listings">
    <div class="listing listing--a" role="img" aria-label="Photo of a red-brick detached house with garden"><span class="sold-tag">SOLD</span></div>
    <div class="listing listing--b" role="img" aria-label="Photo of a white rendered townhouse behind a hedge"><span class="sold-tag">SOLD</span></div>
    <div class="listing listing--c" role="img" aria-label="Photo of a red-brick house with white bay windows"><span class="sold-tag">SOLD</span></div>
  </div>
  <div class="captions">
    <span>Ashcombe Avenue, Hove - 1,100,000 GBP</span>
    <span>Linden Villas, Brighton - 1,350,000 GBP</span>
    <span>Marlow Road, Hove - 1,100,000 GBP</span>
  </div>

  <footer class="contact-footer">
    <div class="brand-name">HOLLIVERS</div>
    <div class="divider"></div>
    <ul class="contact-details">
      <li>01273 555 014</li>
      <li>sales@holliversestateagents.co.uk</li>
      <li>www.holliversestateagents.co.uk</li>
    </ul>
  </footer>
</section>

</body>
</html>
```